Maple Ridge business card design

Card needs to include the following text/items:
Company Logo
Rupert Hollis
Phone # - 517-386-9042
service@mapleridgelandscaping.example
Lawn & landscape maintenance services

```html
<!DOCTYPE html>
<html lang="en">
<head>
<meta charset="utf-8">
<title>Maple Ridge Business Card</title>
<link href="https://fonts.googleapis.com/css2?family=Montserrat:wght@400;500;700&display=swap" rel="stylesheet">
<style>
  :root {
    --backdrop: #b3b3b3;
    --card-white: #ffffff;
    --forest: #0e3a22;
    --lime: #8cba2f;
    --ink-grey: #555555;
    --logo-green: #1f5a2b;
  }
  * { box-sizing: border-box; margin: 0; padding: 0; }
  html, body {
    width: 1200px; height: 900px; overflow: hidden;
    background: var(--backdrop);
    font-family: "Montserrat", sans-serif;
  }
  .stage {
    width: 1200px; height: 900px;
    display: flex; flex-direction: column; align-items: center; justify-content: center;
    gap: 40px;
  }
  .card {
    width: 700px; height: 400px;
    border-radius: 26px;
    position: relative;
    overflow: hidden;
  }
  .card-front { background: var(--card-white); }
  .card-back { background: var(--forest); color: #ffffff; }

  .brand {
    display: flex; align-items: center; gap: 14px;
  }
  .brand-dot {
    width: 56px; height: 56px; border-radius: 50%;
    background: var(--lime);
    flex: none;
  }
  .brand-name {
    font-weight: 700; font-size: 40px; letter-spacing: 0.5px;
  }
  .card-front .brand-name { color: var(--logo-green); }
  .card-back .brand-name { color: #ffffff; font-size: 32px; }
  .card-back .brand-dot { width: 44px; height: 44px; }

  .front-content {
    position: absolute; inset: 0;
    display: flex; flex-direction: column; align-items: center; justify-content: center;
    gap: 22px;
  }
  .tagline {
    font-size: 17px; color: var(--ink-grey); letter-spacing: 0.3px;
  }

  .back-brand { position: absolute; top: 56px; right: 48px; }

  .contact-block { position: absolute; left: 48px; bottom: 44px; }
  .person-name { font-weight: 700; font-size: 30px; color: var(--lime); line-height: 1.1; }
  .person-role { font-size: 17px; margin-top: 4px; }
  .divider { width: 14px; height: 4px; background: var(--lime); margin: 14px 0 14px; }
  .contact-line { display: flex; align-items: center; gap: 12px; font-size: 17px; margin-top: 8px; }
  .contact-line svg { width: 20px; height: 20px; flex: none; }
</style>
</head>
<body>
<main class="stage">
  <section class="card card-front">
    <div class="front-content">
      <div class="brand">
        <span class="brand-dot"></span>
        <span class="brand-name">Maple Ridge</span>
      </div>
      <p class="tagline">Lawn &amp; landscape maintenance services</p>
    </div>
  </section>

  <section class="card card-back">
    <div class="brand back-brand">
      <span class="brand-dot"></span>
      <span class="brand-name">Maple Ridge</span>
    </div>
    <div class="contact-block">
      <p class="person-name">Rupert Hollis</p>
      <p class="person-role">CEO &amp; Founder</p>
      <div class="divider"></div>
      <p class="contact-line">
        <svg viewBox="0 0 24 24" aria-hidden="true"><path fill="#8cba2f" d="M3 9c0-3 4-5 9-5s9 2 9 5v2h-5V9H8v2H3V9zm3 4h12l2 7H4l2-7zm6 1.5a2.5 2.5 0 1 0 0 5 2.5 2.5 0 0 0 0-5z"/></svg>
        <span>517-386-9042</span>
      </p>
      <p class="contact-line">
        <svg viewBox="0 0 24 24" aria-hidden="true"><path fill="#8cba2f" d="M2 5h20v14H2V5zm2 2v.5l8 5 8-5V7H4z"/></svg>
        <span>service@mapleridgelandscaping.example</span>
      </p>
    </div>
  </section>
</main>
</body>
</html>
```